" A Bolsix7 é uma empresa que presta assessoria on-line (via livestream) que é um canal on-line, para investimentos no mercado de açoes e ministra cursos e palestras do nível básico ao avançado. "

```html
<!DOCTYPE html>
<html lang="pt-BR">
<head>
<meta charset="UTF-8">
<title>Bolsix7 — Cartão de visita</title>
<link rel="stylesheet" href="https://fonts.googleapis.com/css2?family=Arimo:wght@400;700&display=swap">
<style>
  :root {
    --stage: #ece7df;
    --card: #ffffff;
    --gold: #b38a2e;
    --gold-light: #e3c77a;
    --gold-dark: #8c6a1e;
    --ink: #3a2a10;
    --text-muted: #8a7a60;
    --text-dark: #4a3a20;
  }
  * { margin: 0; padding: 0; box-sizing: border-box; }
  html, body {
    width: 1200px; height: 1200px; overflow: hidden;
    background: var(--stage);
  }
  .stage { position: relative; width: 1200px; height: 1200px; }
  .card {
    position: absolute; left: 336px; width: 528px; height: 312px;
    background: var(--card);
    box-shadow: 0 6px 18px rgba(60, 40, 10, 0.18);
    overflow: hidden;
  }
  .card--front { top: 228px; }
  .card--back { top: 600px; height: 324px; }
  .brand-name {
    font-family: "Arimo", sans-serif; font-weight: 400;
    color: var(--gold); line-height: 1; white-space: nowrap;
  }
  .card--front .brand-name {
    position: absolute; left: 0; right: 0; top: 164px;
    text-align: center; font-size: 46px;
  }
  .card--back .brand-name {
    position: absolute; left: 26px; top: 72px;
    font-size: 32px;
  }
  .person {
    position: absolute; left: 306px; width: 200px; top: 102px;
    text-align: center; font-family: "Arimo", sans-serif;
  }
  .person__name { font-size: 19px; color: var(--gold-dark); font-weight: 400; }
  .person__role { font-size: 14px; color: var(--text-muted); margin-top: 3px; }
  .person__email { font-size: 14px; color: var(--text-dark); margin-top: 6px; }
  .contact {
    position: absolute; left: 26px; top: 180px;
    font-family: "Arimo", sans-serif; font-size: 14px; line-height: 1.3;
  }
  .contact__phone { color: var(--ink); font-weight: 700; }
  .contact__address { color: var(--text-muted); margin-top: 10px; }
  .web-band {
    position: absolute; left: 0; right: 0; bottom: 0; height: 40px;
    background: linear-gradient(90deg, var(--gold-dark), var(--gold-light) 45%, var(--gold) 70%, var(--gold-light));
    display: flex; align-items: center; justify-content: center;
    font-family: "Arimo", sans-serif; font-size: 17px; letter-spacing: 5px;
    color: var(--ink);
  }
</style>
</head>
<body>
  <main class="stage">
    <section class="card card--front" aria-label="Frente do cartão">
      <div class="brand-name">Bolsix7</div>
    </section>

    <section class="card card--back" aria-label="Verso do cartão">
      <div class="brand-name">Bolsix7</div>
      <div class="person">
        <p class="person__name">Rafael Moura</p>
        <p class="person__role">Função</p>
        <p class="person__email">contato@bolsix7.com.br</p>
      </div>
      <div class="contact">
        <p class="contact__phone">+55 21 3210-4567</p>
        <p class="contact__phone">+55 21 4098-7654</p>
        <div class="contact__address">
          <p>Rua das Acácias, 310 - Centro</p>
          <p>Rio de Janeiro - RJ</p>
          <p>CEP 20040-120</p>
        </div>
      </div>
      <div class="web-band">www.bolsix7.com.br</div>
    </section>
  </main>
</body>
</html>
```